Dermiva clinic Website for young modern clinic

Website for dermiva clinic
To be modern and sleek.
Clinic base - are young and modern.
Images
Main treatments are Dermiva and lip enhancement
Needs to include
Link to Facebook
Link to twitter
Price list
Room for a small brief on each item
Hours
Mon 10-4pm
Tues 10-4pm
Wed 12-8pm
Thurs Quenby Row 0700-4pm
Friday 10- 2pm
Saturday 9am - 2pm
Booking page/calender
Where we are - map
Address:
52 Wexmoor Lane, 4 Fenbrook Parade TN9 4QW
Phone number 0207 384 9102 or 07914385217
Company Name: NPA
Address: 52 Wexmoor Lane, 4 Fenbrook Parade, TN9 4QW
Phone: 0207 384 9102
Website: www.nessapelbourneaesthetics.co.uk
Clinic
3 page

```html
<!DOCTYPE html>
<html lang="en">
<head>
<meta charset="utf-8">
<title>Nessa Pelbourne Aesthetics</title>
<link href="https://fonts.googleapis.com/css2?family=Arvo:wght@400;700&family=Nunito+Sans:wght@400;700&display=swap" rel="stylesheet">
<style>
  :root {
    --ink: #1d1b1c;
    --ring-grey: #9c9c9e;
    --ring-white: #ffffff;
    --text-light: #ffffff;
    --logo-grey: #c9c9c9;
    --accent: #f0a030;
    --sky: #dce9f5;
    --sky-deep: #b9d2ea;
    --skin: #eec3a8;
  }
  * { box-sizing: border-box; margin: 0; padding: 0; }
  html, body { width: 975px; height: 1200px; overflow: hidden; background: #fff; }
  .page {
    position: relative; width: 975px; height: 1200px; overflow: hidden;
    font-family: "Arvo", serif; color: var(--text-light);
  }
  .hero-photo {
    position: absolute; inset: 0;
    background:
      radial-gradient(ellipse 230px 420px at 487px 560px, var(--skin) 0%, #e7bfa6 55%, rgba(231,191,166,0) 100%),
      radial-gradient(ellipse 380px 260px at 487px 1150px, #e9b99c 0%, rgba(233,185,156,0) 100%),
      linear-gradient(180deg, var(--sky) 0%, var(--sky-deep) 55%, var(--sky) 100%);
  }
  .disc {
    position: absolute; border-radius: 50%; background: var(--ink);
    display: flex; flex-direction: column; align-items: center; justify-content: center;
  }
  .disc--large { width: 480px; height: 480px; border: 24px solid var(--ring-white); }
  .disc--top { left: 247px; top: -276px; justify-content: flex-end; padding-bottom: 42px; }
  .disc--left { left: -274px; top: 348px; }
  .disc--right { left: 768px; top: 348px; }
  .disc--bottom { left: 247px; top: 996px; justify-content: flex-start; padding-top: 72px; }

  .brand { text-align: center; color: var(--logo-grey); font-weight: 400; }
  .brand__initials { font-size: 24px; letter-spacing: 3px; margin-bottom: 22px; }
  .brand__name { font-size: 15px; letter-spacing: 3px; line-height: 1.1; }
  .brand__name span { display: block; font-size: 20px; letter-spacing: 3px; }

  .nav-node {
    position: absolute; width: 204px; height: 204px; border-radius: 50%;
    background: var(--ink); border: 12px solid var(--ring-grey);
    display: flex; flex-direction: column; align-items: center; justify-content: center;
    text-decoration: none; color: var(--text-light);
    box-shadow: 0 0 12px rgba(255,255,255,.6);
  }
  .nav-node--home { left: 44px; top: 84px; }
  .nav-node--about { left: 730px; top: 84px; }
  .nav-node--testimonials { left: 46px; top: 892px; }
  .nav-node--contact { left: 730px; top: 892px; }
  .nav-label { font-size: 20px; font-weight: 700; letter-spacing: .3px; margin-top: 10px; }
  .nav-icon { width: 32px; height: 32px; }

  .petal {
    position: absolute; width: 218px; height: 218px; background: var(--ink);
    border: 11px solid var(--ring-grey);
    display: flex; flex-direction: column; align-items: center; justify-content: center;
    text-decoration: none; color: var(--text-light);
  }
  .petal--services { left: 214px; top: 322px; border-radius: 6px 50% 50% 50%; }
  .petal--booking { left: 542px; top: 328px; border-radius: 50% 6px 50% 50%; }
  .petal--hours {
    left: 376px; top: 688px; width: 224px; height: 224px;
    border-radius: 50% 50% 50% 6px; transform: rotate(-30deg);
  }
  .petal-content {
    position: absolute; left: 376px; top: 688px; width: 224px; height: 224px;
    display: flex; flex-direction: column; align-items: center; justify-content: center;
    text-decoration: none; color: var(--text-light);
  }
  .petal-label { font-size: 17px; font-weight: 700; margin-top: 18px; }

  .social-links { position: absolute; left: 45px; top: 490px; }
  .social-links a {
    display: block; width: 37px; height: 37px; border: 1px solid #8a8a8a;
    margin-bottom: 20.5px;
  }
  .social-links .social-feature {
    position: absolute; left: 55px; top: 82px; width: 37px; height: 37px;
    background: var(--ring-white); border: none;
  }
  .social-links .social-feature::after {
    content: ""; position: absolute; left: 15px; top: 11px; width: 7px; height: 15px;
    background: var(--accent); border-radius: 2px;
  }

  .contact-lines { text-align: center; font-size: 18px; line-height: 1.25; margin-right: 190px; }
  .contact-lines p + p { margin-top: 12px; }

  .address {
    font-family: "Nunito Sans", sans-serif; font-weight: 700; font-size: 18px;
    text-align: center; line-height: 1.3; letter-spacing: .2px;
  }
  .copyright {
    font-family: "Nunito Sans", sans-serif; font-size: 9px; margin-top: 42px;
  }
</style>
</head>
<body>
<main class="page">
  <div class="hero-photo" role="img" aria-label="Photo of a client's face held by blue-gloved hands over a soft blue molecular backdrop"></div>

  <header class="disc disc--large disc--top">
    <div class="brand">
      <div class="brand__initials">NPA</div>
      <div class="brand__name">NESSA PELBOURNE<span>AESTHETICS</span></div>
    </div>
  </header>

  <a class="nav-node nav-node--home" href="#">
    <svg class="nav-icon" viewBox="0 0 32 32" aria-hidden="true"><path d="M16 5 3 16h4v11h7v-7h4v7h7V16h4z" fill="#fff"/></svg>
    <span class="nav-label">HOME</span>
  </a>
  <a class="nav-node nav-node--about" href="#">
    <svg class="nav-icon" viewBox="0 0 32 32" aria-hidden="true"><circle cx="16" cy="16" r="12" fill="none" stroke="#fff" stroke-width="4"/><circle cx="16" cy="16" r="5" fill="none" stroke="#fff" stroke-width="2"/><path d="M9 9l4 4M23 9l-4 4M9 23l4-4M23 23l-4-4" stroke="#fff" stroke-width="4"/></svg>
    <span class="nav-label">ABOUT US</span>
  </a>

  <div class="disc disc--large disc--left">
    <nav class="social-links" aria-label="Social links">
      <a href="#" aria-label="Video channel"></a>
      <a href="#" aria-label="Professional network"></a>
      <a href="#" aria-label="News feed"></a>
      <a href="#" aria-label="Photo gallery"></a>
      <a class="social-feature" href="#" aria-label="Community page"></a>
    </nav>
  </div>

  <div class="disc disc--large disc--right">
    <div class="contact-lines">
      <p>Call Today<br>0207 384 9102</p>
      <p>Fax :<br>07914385217</p>
    </div>
  </div>

  <a class="petal petal--services" href="#">
    <svg class="nav-icon" viewBox="0 0 32 32" aria-hidden="true"><circle cx="16" cy="16" r="12" fill="none" stroke="#fff" stroke-width="4"/><circle cx="16" cy="16" r="5" fill="none" stroke="#fff" stroke-width="2"/><path d="M9 9l4 4M23 9l-4 4M9 23l4-4M23 23l-4-4" stroke="#fff" stroke-width="4"/></svg>
    <span class="petal-label">SERVICES</span>
  </a>
  <a class="petal petal--booking" href="#">
    <svg class="nav-icon" viewBox="0 0 32 32" aria-hidden="true"><path d="M7 3h12l7 7v19H7z" fill="none" stroke="#fff" stroke-width="2"/><path d="M19 3v7h7M11 16h11M11 20h11M11 24h11" stroke="#fff" stroke-width="2" fill="none"/></svg>
    <span class="petal-label">BOOKING PAGE</span>
  </a>

  <div class="petal petal--hours" aria-hidden="true"></div>
  <a class="petal-content" href="#">
    <svg class="nav-icon" viewBox="0 0 32 32" aria-hidden="true"><circle cx="16" cy="16" r="12" fill="none" stroke="#fff" stroke-width="3"/><path d="M16 9v8h-5" fill="none" stroke="#fff" stroke-width="3"/></svg>
    <span class="petal-label">WORKING HOUR</span>
  </a>

  <a class="nav-node nav-node--testimonials" href="#">
    <svg class="nav-icon" viewBox="0 0 32 32" aria-hidden="true"><rect x="3" y="7" width="26" height="19" fill="none" stroke="#fff" stroke-width="2.5"/><path d="M3 8l13 10 13-10" fill="none" stroke="#fff" stroke-width="2.5"/></svg>
    <span class="nav-label">TESTIMONILAS</span>
  </a>
  <a class="nav-node nav-node--contact" href="#">
    <svg class="nav-icon" viewBox="0 0 32 32" aria-hidden="true"><path d="M16 3a9 9 0 0 0-9 9c0 7 9 17 9 17s9-10 9-17a9 9 0 0 0-9-9z" fill="#fff"/><circle cx="16" cy="12" r="3.5" fill="#1d1b1c"/></svg>
    <span class="nav-label">CONTACT US</span>
  </a>

  <footer class="disc disc--large disc--bottom">
    <p class="address">52 WEXMOOR LANE,<br>4 FENBROOK PARADE TN9 4QW</p>
    <p class="copyright">Copyright 2015 Comapny Name. All Rights Reserved.</p>
  </footer>
</main>
</body>
</html>
```